Security Services Business Card

Looking for a clean modern style business card design for a residential and commercial security solutions provider. We install and service the following
security alarm, access control, video surveillance and fire alarm. Attached are the front and back of our current business cards in PSD file format.

Target Market(s)

Security alarm clients in the commercial and residential markets

Industry/Entity Type

Security Service

Contact Information for Business Card

We are open to designers suggestion and or design ideas.

Font styles to use
Serif
Sans Serif

Colors
3276b5
33a6d7
fffefd

Requirements
Must have
• Must have company logo , first and last name , phone number , web and email address, ect....

```html
<!DOCTYPE html>
<html lang="en">
<head>
<meta charset="utf-8">
<title>Veridan Systems – Business Card</title>
<link href="https://fonts.googleapis.com/css2?family=Montserrat:wght@400;500;600&display=swap" rel="stylesheet">
<style>
  :root {
    --stage: #545454;
    --paper: #ffffff;
    --ink-dark: #141414;
    --brand-blue: #3a84c5;
    --band-grey: #a2a3a6;
    --muted: #555555;
    --on-blue: #ffffff;
  }
  * { margin: 0; padding: 0; box-sizing: border-box; }
  html, body {
    width: 1200px; height: 1200px; overflow: hidden;
    background: var(--stage);
    font-family: "Montserrat", Arial, sans-serif;
  }
  .card {
    position: absolute; left: 207px; width: 786px; height: 448px; overflow: hidden;
  }
  .card--front { top: 112px; background: var(--paper); }
  .card--back { top: 640px; background: var(--ink-dark); }

  .card__swoosh { position: absolute; inset: 0; width: 786px; height: 448px; }
  .swoosh-grey { fill: var(--band-grey); }
  .swoosh-blue { fill: var(--brand-blue); }

  .brand-name {
    position: absolute; color: var(--brand-blue); font-weight: 600; white-space: nowrap;
  }
  .card--front .brand-name { left: 52px; top: 78px; font-size: 40px; letter-spacing: 0.5px; }
  .card--back .brand-name { left: 0; right: 0; top: 188px; text-align: center; font-size: 56px; letter-spacing: 1px; }

  .person { position: absolute; right: 53px; top: 52px; text-align: right; }
  .person__name { color: var(--brand-blue); font-weight: 500; font-size: 33px; letter-spacing: 0.5px; line-height: 1.1; }
  .person__title { color: var(--muted); font-size: 21px; line-height: 1.3; }

  .contact {
    position: absolute; right: 53px; top: 214px; text-align: right;
    color: var(--on-blue); font-size: 20px; line-height: 27px;
  }
  .contact__address { margin-bottom: 9px; }
  .contact__line { display: flex; justify-content: flex-end; align-items: center; gap: 5px; }
  .contact__icon { width: 13px; height: 13px; fill: none; stroke: var(--on-blue); stroke-width: 1.6; }
</style>
</head>
<body>

<section class="card card--front">
  <svg class="card__swoosh" viewBox="0 0 786 448" aria-hidden="true">
    <path class="swoosh-grey" d="M101,448 C220,280 450,168 786,158 L786,448 Z"/>
    <path class="swoosh-blue" d="M141,448 C262,300 482,176 786,161 L786,448 Z"/>
  </svg>

  <div class="brand-name">Veridan Systems</div>

  <div class="person">
    <div class="person__name">DANIEL HARLOW</div>
    <div class="person__title">Director</div>
  </div>

  <div class="contact">
    <div class="contact__address">
      4810 Lakeview Road<br>
      Suite #210<br>
      Westfield, Ohio 44000
    </div>
    <div class="contact__line">(555) 214-7730
      <svg class="contact__icon" viewBox="0 0 14 14"><rect x="3.5" y="1" width="7" height="12" rx="1.2"/><line x1="6" y1="10.5" x2="8" y2="10.5"/></svg>
    </div>
    <div class="contact__line">(800) 555-0192 (Toll-Free)
      <svg class="contact__icon" viewBox="0 0 14 14"><path d="M3 1.5 L5.5 1.5 L6 4.5 L4.5 5.5 C5.3 7.5 6.5 8.8 8.5 9.6 L9.5 8 L12.5 8.5 L12.5 11 C12.5 12 11.5 12.8 10.5 12.5 C6 11.5 2.5 8 1.5 3.5 C1.3 2.5 2 1.5 3 1.5 Z"/></svg>
    </div>
    <div class="contact__line">info@veridansystems.com
      <svg class="contact__icon" viewBox="0 0 14 14"><rect x="1" y="3" width="12" height="8" rx="1"/><polyline points="1.5,3.5 7,8 12.5,3.5"/></svg>
    </div>
    <div class="contact__line">www.veridansystems.com
      <svg class="contact__icon" viewBox="0 0 14 14"><circle cx="7" cy="7" r="5.8"/><ellipse cx="7" cy="7" rx="2.6" ry="5.8"/><line x1="1.2" y1="7" x2="12.8" y2="7"/><line x1="2" y1="4.2" x2="12" y2="4.2"/><line x1="2" y1="9.8" x2="12" y2="9.8"/></svg>
    </div>
  </div>
</section>

<section class="card card--back">
  <div class="brand-name">Veridan Systems</div>
</section>

</body>
</html>
```